Safety training business card design

We need a buisness card design and logo for a small buisness that provides safety training through out the mining and civil construction industries. We provide first aid , confined space working at heights , machinery tickets, chainsaw, four wheel drive and four wheel motorbike training. We would like to use the design colors of navy blue, Fluro or lime green and white .

Industry/Entity Type

Construction

Contact Information for Business Card

Kelbrook Earthmoving & Training , Dennis Holloway, kelbrook.training@mailbox-example.com, ph 0438615044 abn 47 816 305 971

```html
<!DOCTYPE html>
<html lang="en">
<head>
<meta charset="utf-8">
<title>Kelbrook Earthmoving &amp; Training – Business Card</title>
<link rel="stylesheet" href="https://fonts.googleapis.com/css2?family=Roboto:wght@300;400;500&display=swap">
<style>
  :root {
    --navy: #0a1a3d;
    --lime: #8dc63f;
    --white: #ffffff;
    --stage: #cbcbcb;
  }
  * { margin: 0; padding: 0; box-sizing: border-box; }
  html, body {
    width: 1200px;
    height: 1000px;
    overflow: hidden;
    background: var(--stage);
    font-family: "Roboto", Arial, sans-serif;
  }
  .card {
    position: absolute;
    left: 238px;
    width: 722px;
    height: 417px;
    background: var(--white);
    overflow: hidden;
  }
  .card--front { top: 57px; }
  .card--back { top: 528px; }

  /* Front: wordmark */
  .wordmark {
    position: absolute;
    left: 263px;
    top: 0;
    color: var(--navy);
    font-weight: 500;
  }
  .brand-square {
    position: absolute;
    left: 26px;
    top: 78px;
    width: 40px;
    height: 40px;
    background: var(--lime);
  }
  .wordmark__name {
    position: absolute;
    left: 84px;
    top: 50px;
    font-size: 84px;
    line-height: 1;
    letter-spacing: -1px;
    white-space: nowrap;
  }
  .wordmark__sub {
    position: absolute;
    left: 137px;
    top: 138px;
    font-size: 47px;
    line-height: 1;
    white-space: nowrap;
  }
  .wordmark-wrap {
    position: absolute;
    left: 0;
    top: 0;
    color: var(--navy);
    font-weight: 500;
  }

  .swoosh {
    position: absolute;
    left: 0;
    top: 236px;
    width: 722px;
    height: 22px;
  }
  .contact-band {
    position: absolute;
    left: 0;
    top: 256px;
    width: 722px;
    height: 161px;
    background: var(--navy);
    color: var(--white);
  }
  .contact-band__person {
    position: absolute;
    left: 68px;
    top: 62px;
    font-size: 28px;
    font-weight: 400;
    white-space: nowrap;
  }
  .contact-band__divider {
    position: absolute;
    left: 339px;
    top: 60px;
    width: 3px;
    height: 60px;
    background: var(--lime);
  }
  .contact-band__details {
    position: absolute;
    left: 364px;
    top: 38px;
    list-style: none;
    font-size: 19.5px;
    line-height: 35px;
    white-space: nowrap;
  }

  /* Back */
  .back-brand {
    position: absolute;
    left: 28px;
    top: 320px;
    display: flex;
    align-items: center;
    gap: 14px;
    color: var(--navy);
    font-size: 42px;
    font-weight: 500;
    line-height: 1;
  }
  .back-brand__square {
    width: 34px;
    height: 34px;
    background: var(--lime);
  }
  .tagline {
    position: absolute;
    left: 234px;
    top: 110px;
    font-size: 34px;
    line-height: 39px;
    font-weight: 300;
    color: var(--navy);
    white-space: nowrap;
  }
  .tagline__accent {
    color: var(--lime);
    font-weight: 400;
  }
</style>
</head>
<body>

<section class="card card--front" aria-label="Business card front">
  <div class="wordmark-wrap">
    <span class="brand-square"></span>
    <span class="wordmark__name">Kelbrook</span>
    <span class="wordmark__sub">Earthmoving &amp; Training</span>
  </div>

  <svg class="swoosh" viewBox="0 0 722 22" preserveAspectRatio="none" aria-hidden="true">
    <path d="M60 21 C 250 8, 520 0, 700 21 Z" fill="var(--lime)"/>
  </svg>

  <div class="contact-band">
    <p class="contact-band__person">Dennis Holloway</p>
    <span class="contact-band__divider"></span>
    <ul class="contact-band__details">
      <li>Ph: 0438 615 044</li>
      <li>kelbrook.training@mailbox-example.com</li>
      <li>ABN: 47 816 305 971</li>
    </ul>
  </div>
</section>

<section class="card card--back" aria-label="Business card back">
  <p class="tagline">
    Providing <span class="tagline__accent">Quality Training</span><br>
    with <span class="tagline__accent">Professional Service</span>
  </p>
  <div class="back-brand">
    <span class="back-brand__square"></span>
    <span>Kelbrook</span>
  </div>
</section>

</body>
</html>
```